BRIGHT LEDGER NOW

I'm virtually ready to launch my site, but I have a number of edits and modifications that need to be implemented. More importantly, I'm always looking to improve my site, particularly now that I am making my proverbial "FIRST IMPRESSION." Thus, I'm willing to see if there is someone who can add creativity and perhaps improve what I already have, particularly on the All Important Front Page.

Need extra days to review

```html
<!DOCTYPE html>
<html lang="en">
<head>
<meta charset="utf-8">
<title>Bright Ledger Now</title>
<link rel="stylesheet" href="https://fonts.googleapis.com/css2?family=Poppins:ital,wght@0,400;0,500;0,600;0,700;1,500&display=swap">
<style>
:root{
  --navy:#0d2350;
  --red:#a8172c;
  --white:#ffffff;
  --ink:#3b3b45;
  --muted:#6a6a72;
  --panel:#f1f1f2;
  --hero-dark:#1c1512;
  --hero-warm:#5a4130;
  --footer:#1f1d22;
}
*{margin:0;padding:0;box-sizing:border-box}
html,body{width:1200px;height:3767px;overflow:hidden}
body{position:relative;background:var(--white);font-family:"Poppins",sans-serif;color:var(--ink)}

/* hero */
.hero{position:absolute;left:0;top:0;width:1200px;height:720px}
.hero-photo{position:absolute;left:0;top:0;width:1200px;height:700px;
  background:radial-gradient(ellipse at 35% 20%,#8a6a4c 0%,var(--hero-warm) 25%,#2e221b 60%,var(--hero-dark) 100%)}
.hero-shade{position:absolute;inset:0;background:rgba(10,8,8,.35)}
.hero-curve{position:absolute;left:0;top:0}
.brand-mark{position:absolute;display:flex;align-items:center;gap:10px;font-weight:600;color:var(--white);font-size:14px;letter-spacing:.5px}
.brand-dot{width:40px;height:40px;border-radius:50%;background:var(--red)}
.nav{position:absolute;top:40px;left:0;width:1200px;height:26px}
.nav a{position:absolute;color:var(--white);text-decoration:none;font-size:17px;top:0}
.phone-pill{position:absolute;left:1014px;top:37px;width:113px;height:33px;border-radius:17px;background:var(--red);color:var(--white);font-size:14px;font-weight:600;display:flex;align-items:center;justify-content:center}
.hero-title{position:absolute;top:240px;width:1200px;text-align:center;color:var(--white);font-size:52px;font-weight:700;letter-spacing:1px}
.hero-sub{position:absolute;top:315px;width:1200px;text-align:center;color:var(--white);font-size:20px;line-height:24.5px}
.btn-pill{position:absolute;left:500px;top:425px;width:183px;height:56px;border-radius:28px;background:var(--red);color:var(--white);font-size:17px;font-weight:500;display:flex;align-items:center;justify-content:center}

/* headings */
.section-title{position:absolute;color:var(--navy);font-weight:700;font-size:36px;letter-spacing:.5px}
.rule{position:absolute;height:3px;background:var(--navy)}

/* about */
.photo{position:absolute}
.about-back{left:158px;top:799px;width:428px;height:328px;border-radius:40px;background:linear-gradient(135deg,#d9dde0,#9aa3aa 55%,#2c2d33)}
.about-front{left:114px;top:1010px;width:263px;height:241px;border-radius:40px 0 40px 0;background:linear-gradient(160deg,#e9e6e0,#8d7d6c 60%,#2a2a30)}
.exp-badge{position:absolute;left:253px;top:1102px;width:251px;height:85px;border-radius:10px;background:var(--navy);color:var(--white);display:flex;align-items:center;gap:14px;padding-left:16px}
.exp-num{font-size:46px;font-weight:700}
.exp-label{font-size:19px;font-weight:500;line-height:20px}
.body-copy{position:absolute;font-size:10.5px;line-height:16px;color:var(--ink)}
.body-copy p{margin-bottom:6px}
.btn-slant{position:absolute;height:43px;background:var(--red);color:var(--white);font-size:17px;font-weight:500;display:flex;align-items:center;justify-content:center;clip-path:polygon(16px 0,100% 0,100% 100%,0 100%)}

/* services */
.panel{position:absolute;left:0;width:1200px;background:var(--panel)}
.service-card{position:absolute;width:284px;height:260px;background:var(--white);border-radius:36px;box-shadow:0 10px 24px rgba(0,0,0,.08);text-align:center}
.service-thumb{position:absolute;left:72px;top:-44px;width:140px;height:140px;border-radius:50%}
.service-name{position:absolute;left:0;top:108px;width:284px;font-size:18.5px;font-weight:600;color:#111;line-height:19px}
.service-text{position:absolute;left:12px;top:155px;width:260px;font-size:9.3px;line-height:13.5px;color:var(--muted)}
.read-more{position:absolute;left:74px;bottom:-13px;width:146px;height:26px;background:var(--navy);color:var(--white);font-size:12px;font-weight:500;display:flex;align-items:center;justify-content:center;clip-path:polygon(14px 0,100% 0,100% 100%,0 100%)}
.thumb-scale{background:radial-gradient(circle at 40% 40%,#c9a27d,#6b3f28 60%,#2a1710)}
.thumb-gavel{background:radial-gradient(circle at 50% 60%,#a36b40,#5a2e1a 60%,#24120b)}
.thumb-tech{background:radial-gradient(circle at 45% 60%,#8fb6e6,#2d5fa0 55%,#0c1d3d)}
.thumb-man{background:radial-gradient(circle at 50% 40%,#d8c6b2,#8d7a66 60%,#3b3229)}
.thumb-money{background:radial-gradient(circle at 50% 50%,#b9a58c,#6d4b33 55%,#3a2a1f)}
.thumb-desk{background:radial-gradient(circle at 50% 50%,#e6e1da,#8b7560 60%,#3b2a1e)}

/* case study */
.case-photo{left:728px;top:2366px;width:323px;height:249px;border-radius:40px;background:linear-gradient(135deg,#c9cdb8,#93a084 45%,#c98a56 80%,#8a6b4b)}
.quote{position:absolute;left:728px;top:2624px;width:323px;text-align:center;font-style:italic;font-weight:500;color:#6d6d72;font-size:14px;line-height:20px}
.quote-author{position:absolute;left:728px;top:2670px;width:323px;text-align:center;font-weight:600;color:var(--navy);font-size:14px}

/* faq */
.faq-item{position:absolute;width:472px;height:69px;border:1.5px solid var(--navy);border-radius:12px;display:flex;align-items:center;justify-content:space-between;padding:0 18px;color:var(--navy);font-size:12px;font-weight:600;line-height:15px}
.faq-arrow{flex:none;width:27px;height:27px}

/* footer */
.footer-curve{position:absolute;left:0;top:3280px}
.footer-heading{position:absolute;color:var(--white);font-size:17px;font-weight:500}
.footer-link{position:absolute;color:var(--white);font-size:17px}
.social{position:absolute;top:3630px;width:20px;height:20px;border-radius:50%;background:var(--white)}
.contact-row{position:absolute;left:800px;display:flex;align-items:center;gap:10px;color:var(--white);font-size:14px;line-height:18px}
.contact-icon{flex:none;width:34px;height:34px}
.footer-line{position:absolute;left:100px;top:3707px;width:945px;height:1px;background:var(--red)}
.copyright{position:absolute;top:3726px;width:1200px;text-align:center;color:var(--white);font-size:14px}
</style>
</head>
<body>

<header class="hero">
  <div class="hero-photo" role="img" aria-label="Courtroom interior with a lawyer addressing the bench in warm light"><div class="hero-shade"></div></div>
  <svg class="hero-curve" width="1200" height="730" viewBox="0 0 1200 730">
    <path d="M0,548 Q600,782 1200,548 L1200,730 L0,730 Z" fill="#ffffff"/>
    <path d="M0,577 Q600,797 1200,577" fill="none" stroke="#0d2350" stroke-width="11"/>
    <circle cx="600" cy="684" r="42" fill="#0d2350" stroke="#ffffff" stroke-width="4"/>
  </svg>
  <div class="brand-mark" style="left:68px;top:32px"><span class="brand-dot"></span>BRIGHT LEDGER NOW</div>
  <nav class="nav">
    <a style="left:328px">HOME</a>
    <a style="left:441px">ABOUT</a>
    <a style="left:552px">SERVICES</a>
    <a style="left:682px">FAQs</a>
    <a style="left:766px">CONTACT</a>
  </nav>
  <div class="phone-pill">480.555.0192</div>
  <h1 class="hero-title">BRIGHT LEDGER NOW</h1>
  <p class="hero-sub">We are devoted to PREVENTING LEGAL CLAIMS and<br>COSTLY LAWSUITS through a variety of FREE and<br>VERY AFFORDABLE services</p>
  <div class="btn-pill">CONTACT US</div>
</header>

<section class="about">
  <div class="photo about-back" role="img" aria-label="Businesswoman smiling in a meeting with a client by a window"></div>
  <div class="photo about-front" role="img" aria-label="Smiling businessman holding out a set of keys"></div>
  <div class="exp-badge"><span class="exp-num">10+</span><span class="exp-label">Years of<br>Experience</span></div>
  <h2 class="section-title" style="left:661px;top:845px">ABOUT US</h2>
  <div class="rule" style="left:661px;top:893px;width:131px"></div>
  <div class="body-copy" style="left:661px;top:920px;width:450px">
    <p>BLN is a group of attorney and legal assistants with many years of experience in litigation, who are devoted to PREVENTING LEGAL CLAIMS and COSTLY LAWSUITS through a variety of FREE and VERY AFFORDABLE services</p>
    <p>OUR UNIQUE SERVICE PLAN MAKES IT POSSIBLE FOR US TO HALT COSTLY CLAIMS.</p>
    <p>In our vast experience with commercial litigation, we believe that a very large percentage of litigation cases hinge on "he said / she said" issues. By using BLN's services, we believe we can INSULATE you and your business from all such issues, which will MINIMIZE your EXPOSURE to LEGAL CLAIMS and LAWSUITS.</p>
  </div>
  <div class="btn-slant" style="left:666px;top:1089px;width:297px">GET A FREE CONSULTATION</div>
</section>

<section class="panel" style="top:1337px;height:936px"></section>
<h2 class="section-title" style="left:0;width:1160px;text-align:center;top:1384px">SERVICES</h2>
<div class="rule" style="left:497px;top:1432px;width:162px"></div>

<article class="service-card" style="left:115px;top:1538px">
  <div class="service-thumb thumb-scale" role="img" aria-label="Hand beside the scales of justice"></div>
  <h3 class="service-name">FREE INITIAL<br>CONSULTATION</h3>
  <p class="service-text">As a prospective Bright Ledger Now ("BLN") member, we urge you to schedule an initial consultation with us – at no charge – where we will go over each of the services in detail, and offer an overview of your business formation at no charge.</p>
  <div class="read-more">READ MORE</div>
</article>
<article class="service-card" style="left:453px;top:1538px">
  <div class="service-thumb thumb-gavel" role="img" aria-label="Judge's gavel resting on a law book"></div>
  <h3 class="service-name">PROPRIETARY CONTRACT<br>LANGUAGE</h3>
  <p class="service-text">As a prospective Bright Ledger Now ("BLN") member, we urge you to schedule an initial consultation with us – at no charge – where we will go over each of the services in detail, and offer an overview of your business formation at no charge.</p>
  <div class="read-more">READ MORE</div>
</article>
<article class="service-card" style="left:794px;top:1538px">
  <div class="service-thumb thumb-tech" role="img" aria-label="Finger touching a glowing consultation screen"></div>
  <h3 class="service-name">FREE<br>CONSULTATION</h3>
  <p class="service-text">As a prospective Bright Ledger Now ("BLN") member, we urge you to schedule an initial consultation with us – at no charge – where we will go over each of the services in detail, and offer an overview of your business formation at no charge.</p>
  <div class="read-more">READ MORE</div>
</article>
<article class="service-card" style="left:127px;top:1907px">
  <div class="service-thumb thumb-man" role="img" aria-label="Man in a suit reading a letter"></div>
  <h3 class="service-name">FREE ATTORNEY<br>LETTERS</h3>
  <p class="service-text">As a prospective Bright Ledger Now ("BLN") member, we urge you to schedule an initial consultation with us – at no charge – where we will go over each of the services in detail, and offer an overview of your business formation at no charge.</p>
  <div class="read-more">READ MORE</div>
</article>
<article class="service-card" style="left:465px;top:1907px">
  <div class="service-thumb thumb-money" role="img" aria-label="Gavel lying on banknotes"></div>
  <h3 class="service-name">LITIGATION<br>DISCOUNTS</h3>
  <p class="service-text">As a prospective Bright Ledger Now ("BLN") member, we urge you to schedule an initial consultation with us – at no charge – where we will go over each of the services in detail, and offer an overview of your business formation at no charge.</p>
  <div class="read-more">READ MORE</div>
</article>
<article class="service-card" style="left:805px;top:1907px">
  <div class="service-thumb thumb-desk" role="img" aria-label="Hands at a desk beside the scales of justice"></div>
  <h3 class="service-name" style="top:118px">COLLECTIONS</h3>
  <p class="service-text">As a prospective Bright Ledger Now ("BLN") member, we urge you to schedule an initial consultation with us – at no charge – where we will go over each of the services in detail, and offer an overview of your business formation at no charge.</p>
  <div class="read-more">READ MORE</div>
</article>

<section class="case-study">
  <h2 class="section-title" style="left:115px;top:2362px">CASE STUDY</h2>
  <div class="rule" style="left:115px;top:2410px;width:167px"></div>
  <div class="body-copy" style="left:115px;top:2438px;width:485px">
    A homebuilding company was sued by a former employee who claimed to have been promised a more favorable sales area, which claim was disputed by the homebuilder. There was no evidence that such a promise had been made, other than the plaintiff's oral testimony. The company had the case dismissed, but spent $10,000 defending the case.<br>
    And even though it was awarded its attorney's fees, the plaintiff proved uncollectible. Had the company been an BLN member, the case likely would never have been filed. Call for your FREE CONSULTATION and let us show you why the plaintiff likely would not have found a contingency attorney (as was the case) or been able to pay an attorney on an hourly basis. In short, by using BLN's services, the plaintiff's claim would not have been filed.
  </div>
  <div class="btn-slant" style="left:101px;top:2640px;width:297px">GET A FREE CONSULTATION</div>
  <div class="photo case-photo" role="img" aria-label="Close-up of a banknote portrait wearing a face mask"></div>
  <p class="quote">An OUNCE of PREVENTION is<br>worth a POUND of CURE.</p>
  <p class="quote-author">Harold Whitcombe</p>
</section>

<section class="panel" style="top:2777px;height:560px"></section>
<h2 class="section-title" style="left:0;width:1152px;text-align:center;top:2823px;font-size:34px">FREQUENTLY ASKED QUESTIONS</h2>
<div class="rule" style="left:421px;top:2875px;width:305px"></div>

<div class="faq-item" style="left:101px;top:2964px"><span>Why should I be concerned about legal claims?</span><svg class="faq-arrow" viewBox="0 0 27 27"><circle cx="13.5" cy="13.5" r="13" fill="#0d2350"/><path d="M7 13.5h11M13.5 8.5l5 5-5 5" stroke="#fff" stroke-width="2.4" fill="none" stroke-linecap="round" stroke-linejoin="round"/></svg></div>
<div class="faq-item" style="left:621px;top:2964px"><span>Provide more details about the value of BLN's<br>contract language.</span><svg class="faq-arrow" viewBox="0 0 27 27"><circle cx="13.5" cy="13.5" r="13" fill="#0d2350"/><path d="M7 13.5h11M13.5 8.5l5 5-5 5" stroke="#fff" stroke-width="2.4" fill="none" stroke-linecap="round" stroke-linejoin="round"/></svg></div>
<div class="faq-item" style="left:103px;top:3062px"><span>If I'm a contractor, for example, how can an BLN<br>membership minimize legal claims against my business?</span><svg class="faq-arrow" viewBox="0 0 27 27"><circle cx="13.5" cy="13.5" r="13" fill="#0d2350"/><path d="M7 13.5h11M13.5 8.5l5 5-5 5" stroke="#fff" stroke-width="2.4" fill="none" stroke-linecap="round" stroke-linejoin="round"/></svg></div>
<div class="faq-item" style="left:623px;top:3062px"><span>What does an BLN membership cost?</span><svg class="faq-arrow" viewBox="0 0 27 27"><circle cx="13.5" cy="13.5" r="13" fill="#0d2350"/><path d="M7 13.5h11M13.5 8.5l5 5-5 5" stroke="#fff" stroke-width="2.4" fill="none" stroke-linecap="round" stroke-linejoin="round"/></svg></div>
<div class="faq-item" style="left:105px;top:3158px"><span>Do you have a Referral Program?</span><svg class="faq-arrow" viewBox="0 0 27 27"><circle cx="13.5" cy="13.5" r="13" fill="#0d2350"/><path d="M7 13.5h11M13.5 8.5l5 5-5 5" stroke="#fff" stroke-width="2.4" fill="none" stroke-linecap="round" stroke-linejoin="round"/></svg></div>
<div class="faq-item" style="left:626px;top:3158px"><span>Do you have a Referral Program?</span><svg class="faq-arrow" viewBox="0 0 27 27"><circle cx="13.5" cy="13.5" r="13" fill="#0d2350"/><path d="M7 13.5h11M13.5 8.5l5 5-5 5" stroke="#fff" stroke-width="2.4" fill="none" stroke-linecap="round" stroke-linejoin="round"/></svg></div>

<footer>
  <svg class="footer-curve" width="1200" height="487" viewBox="0 0 1200 487" role="img" aria-label="Dim office backdrop with a woman on the phone">
    <path d="M0,132 Q600,-40 1200,132 L1200,487 L0,487 Z" fill="#1f1d22"/>
    <path d="M0,126 Q600,-46 1200,126" fill="none" stroke="#a8172c" stroke-width="9"/>
  </svg>
  <div class="brand-mark" style="left:76px;top:3512px"><span class="brand-dot" style="width:50px;height:50px"></span>BRIGHT LEDGER NOW</div>
  <span class="social" style="left:75px" aria-label="Social profile one"></span>
  <span class="social" style="left:121px" aria-label="Social profile two"></span>
  <span class="social" style="left:170px" aria-label="Social profile three"></span>
  <span class="social" style="left:219px" aria-label="Social profile four"></span>

  <h4 class="footer-heading" style="left:441px;top:3478px">QUICK LINKS</h4>
  <a class="footer-link" style="left:443px;top:3519px">Home</a>
  <a class="footer-link" style="left:443px;top:3563px">About</a>
  <a class="footer-link" style="left:441px;top:3607px">Services</a>
  <a class="footer-link" style="left:441px;top:3651px">Contact Us</a>

  <h4 class="footer-heading" style="left:807px;top:3478px">CONTACT INFO</h4>
  <div class="contact-row" style="top:3527px"><svg class="contact-icon" viewBox="0 0 34 34"><circle cx="17" cy="17" r="15" fill="none" stroke="#a8172c" stroke-width="2.5"/><path d="M12 10l3 0 1.5 4-2 1.5a9 9 0 0 0 4 4l1.5-2 4 1.5 0 3a2 2 0 0 1-2 2A13 13 0 0 1 10 12a2 2 0 0 1 2-2z" fill="#a8172c"/></svg>(480) 555-0147</div>
  <div class="contact-row" style="top:3580px"><svg class="contact-icon" viewBox="0 0 34 34"><circle cx="17" cy="17" r="15" fill="none" stroke="#a8172c" stroke-width="2.5"/><path d="M12 10l3 0 1.5 4-2 1.5a9 9 0 0 0 4 4l1.5-2 4 1.5 0 3a2 2 0 0 1-2 2A13 13 0 0 1 10 12a2 2 0 0 1 2-2z" fill="#a8172c"/></svg>(800) 555-0163</div>
  <div class="contact-row" style="top:3639px"><svg class="contact-icon" viewBox="0 0 34 34"><circle cx="17" cy="17" r="15" fill="none" stroke="#a8172c" stroke-width="2.5"/><path d="M17 8a6 6 0 0 1 6 6c0 5-6 11-6 11s-6-6-6-11a6 6 0 0 1 6-6z" fill="#a8172c"/><circle cx="17" cy="14" r="2.2" fill="#1f1d22"/></svg>4820 ALDER CREST BLVD., SUITE 210,<br>FAIRHAVEN, ARIZONA 85000</div>
  <div class="footer-line"></div>
  <p class="copyright">Copyright © 2021. All rights reserved.</p>
</footer>

</body>
</html>
```